Mind-Body Counsellor Needs a Flyer

Please refer to the attachment for the content of the flyer.

I need a 99x210mm double sided leaflet design for my Vancouver BC based counselling practice.

I am a somatic counsellor who helps people with chronic body symptoms transform their experiences by working on the emotional, historical and relational aspects of the body difficulty. I use art, movement and body awareness in my practice to support and follow my client's unique process. I believe in the power and creativity of the body symptoms itself to show a needed direction. My clients report that this process is transformational, and helps change the relationship they have with their symptom. Often the symptom itself is relieved as the person integrates the needed changes in their life. People say they feel more alive, whole and aware of their overall path in life through this process. I am trained in Lantern Weave Therapy.

I will be bringing the flyer to Doctors and Massage Therapists offices to get new referrals of clients who seek pain management with no relief in the conventional medical system. I would like designs that show diversity of cultures and body types. The final design should communicate professionalism, creativity, hope and healing.
Updates

Reason: Travelling and unable to check in as frequently!

Target Market(s)

Physician and health practitioners who can refer clients with difficulties relating to anxiety, depression, and medically untreatable body symptoms

Industry/Entity Type

Counsellor

Font styles to use
Sans Serif

Colors
ffcf3e
ffc214
fbee3d
cadf82
acd037
9bcb3c

Requirements
Must have
• Visual impact
• A sense of hope and transformation
• Sense of professionalism and creativity
Nice to have
• May or may not include people - but if it does, must represent diverse genders, ages, races, abilities etc.
Should not have
• Too text heavy
• For some reason the uploader is not working - I'll get the text uploaded by tomorrow!

```html
<!DOCTYPE html>
<html lang="en">
<head>
<meta charset="utf-8">
<title>Elise Marchand – Counselling Flyer</title>
<link href="https://fonts.googleapis.com/css2?family=Source+Sans+3:wght@400;600;700&family=Oswald:wght@700&family=Schoolbell&display=swap" rel="stylesheet">
<style>
:root{
  --backdrop:#754c2c;
  --leaf:#9bcb3c;
  --leaf-light:#cadf82;
  --leaf-mid:#acd037;
  --sun:#ffc214;
  --sun-soft:#ffcf3e;
  --lemon:#f5ef3e;
  --ink:#1b1b1b;
  --white:#ffffff;
}
*{box-sizing:border-box;margin:0;padding:0}
html,body{width:1200px;height:1178px;overflow:hidden;background:var(--backdrop)}
body{position:relative;font-family:"Source Sans 3",sans-serif}
.panel{position:absolute;width:457px;height:970px;background:var(--leaf);box-shadow:4px 5px 8px rgba(0,0,0,.45)}
.panel--back{left:140px;top:95px}
.panel--front{left:638px;top:90px}

.section-title{position:absolute;left:31px;font-weight:700;font-size:20.5px;line-height:23px;color:var(--ink)}
.checklist{position:absolute;left:31px;list-style:none}
.checklist li{display:flex;align-items:center;font-size:15px;color:var(--white);white-space:nowrap}
.checklist--quals li{height:24.5px}
.checklist--needs li{height:23.6px}
.checklist .tick{width:14px;height:14px;margin-right:9px;flex:none}

.testimonials{position:absolute;left:0;top:370px;width:457px;height:381px;background:var(--lemon);padding:0 38px 0 31px;box-shadow:0 4px 6px rgba(0,0,0,.25)}
.testimonials h2{font-family:"Schoolbell",cursive;font-weight:400;font-size:37px;color:var(--ink);transform:rotate(-2deg);transform-origin:left;line-height:46px;margin-top:10px;margin-bottom:13px;white-space:nowrap}
.quote{font-size:15.2px;line-height:21px;color:var(--ink);text-align:justify}
.quote cite{display:block;text-align:right;font-style:normal;font-weight:700;font-size:15px}
.quote-rule{height:3px;background:var(--leaf);margin:8px -7px 12px -3px}

.contact{position:absolute;left:0;top:766px;width:457px;text-align:center;color:var(--ink)}
.contact h2{font-weight:400;font-size:29px;color:var(--white);line-height:34px;margin-bottom:1px}
.contact p{font-size:17px;line-height:23px}
.contact .email{font-weight:700;font-size:17.6px;letter-spacing:1px;color:var(--white);margin-top:8px}
.contact .call{font-size:30px;color:var(--white);line-height:38px;margin-top:1px}
.contact .call strong{font-size:32px}

.name{position:absolute;top:29px;width:100%;text-align:center;font-weight:400;font-size:45px;color:var(--white);line-height:50px}
.credentials{position:absolute;top:80px;width:100%;text-align:center;font-size:20px;color:var(--white)}
.hero{position:absolute;left:0;top:120px;width:457px;height:520px}
.motto{position:absolute;top:646px;width:100%;text-align:center;font-family:"Oswald",sans-serif;font-weight:700;font-size:42px;line-height:48px;color:var(--white);text-shadow:2px 2px 3px rgba(0,0,0,.45);letter-spacing:-.5px}
.bio{position:absolute;left:32px;top:766px;width:393px;color:var(--white);font-size:13.8px;line-height:19.5px;text-align:justify}
.bio p+p{margin-top:10px}
</style>
</head>
<body>
<svg width="0" height="0" style="position:absolute">
  <symbol id="tick" viewBox="0 0 14 14">
    <circle cx="7" cy="7" r="6.3" fill="#f4f4f4" stroke="#888" stroke-width="1"/>
    <path d="M3.8 7.2l2.3 2.4 4.4-5.4" fill="none" stroke="#222" stroke-width="2" stroke-linecap="round" stroke-linejoin="round"/>
  </symbol>
</svg>

<section class="panel panel--back">
  <h2 class="section-title" style="top:22px">Qualifications:</h2>
  <ul class="checklist checklist--quals" style="top:52px">
    <li><svg class="tick"><use href="#tick"/></svg>MA Health Promotion</li>
    <li><svg class="tick"><use href="#tick"/></svg>MEd Counselling Psychology</li>
    <li><svg class="tick"><use href="#tick"/></svg>MA Lantern Weave Therapy and Conflict Facilitation</li>
    <li><svg class="tick"><use href="#tick"/></svg>Level 1 Rootline Somatic Therapy</li>
  </ul>
  <h2 class="section-title" style="top:172px">Uniquely Suited for Clients who<br>struggle with:</h2>
  <ul class="checklist checklist--needs" style="top:231px">
    <li><svg class="tick"><use href="#tick"/></svg>Anxiety or depression related to health concerns</li>
    <li><svg class="tick"><use href="#tick"/></svg>Trauma-related difficulties of mind, body or spirit</li>
    <li><svg class="tick"><use href="#tick"/></svg>Chronic, undiagnosed somatic complaints</li>
    <li><svg class="tick"><use href="#tick"/></svg>Nightmares</li>
    <li><svg class="tick"><use href="#tick"/></svg>Relationship conflicts</li>
  </ul>

  <div class="testimonials">
    <h2>What Elise's Clients Say</h2>
    <blockquote class="quote">Elise helped me radically shift how I relate to my body difficulties. They used to be monsters that scared me, now I see them as allies helping me bring my passion out into the world.
      <cite>– Participant in “Inner Compass” Course</cite></blockquote>
    <div class="quote-rule"></div>
    <blockquote class="quote">“I used to have nightmares every night. Working with Elise helped me find the power in my dreams, my history, my struggle to be who I am in the world. Now my dreams are guides telling me I’m on the right track.”
      <cite>- M. K. Business Owner, Trauma Survivor</cite></blockquote>
    <div class="quote-rule"></div>
    <blockquote class="quote">“Working with Elise is magic!!”
      <cite>– R.T. Medical Lab Assistant</cite></blockquote>
  </div>

  <div class="contact">
    <h2>Contact Us:</h2>
    <p>Elise Marchand, MA, MEd</p>
    <p>Counselling Psychology</p>
    <p>Vancouver, BC</p>
    <p class="email">elise.marchand@mailbox.ca</p>
    <p class="call">Call: <strong>778-555-0142</strong></p>
  </div>
</section>

<section class="panel panel--front">
  <h1 class="name">Elise Marchand</h1>
  <p class="credentials">MA, MEd, Registered Clinical Counsellor</p>
  <svg class="hero" viewBox="0 0 457 520">
    <defs>
      <radialGradient id="forest-glow" cx="0.55" cy="0.4" r="0.6">
        <stop offset="0" stop-color="#f3f7b0"/>
        <stop offset="0.35" stop-color="#b9c95a"/>
        <stop offset="0.75" stop-color="#4f6b2a"/>
        <stop offset="1" stop-color="#2e4420"/>
      </radialGradient>
    </defs>
    <path d="M0 60 C140 20 300 10 457 90 L457 110 C300 40 140 60 0 140Z" fill="#6a9a2a"/>
    <path d="M0 75 C140 35 300 25 457 95 L457 110 C300 45 140 70 0 140Z" fill="var(--leaf-light)"/>
    <path d="M0 115 C120 45 300 30 457 98 L457 110 C300 52 130 68 0 140Z" fill="var(--sun)"/>
    <path d="M0 140 C130 65 300 50 457 110 L457 400 C330 470 170 430 0 460Z" fill="url(#forest-glow)" role="img" aria-label="Photo of a sunlit forest path winding through a tunnel of trees"/>
    <path d="M0 460 C170 430 330 470 457 400 L457 430 C330 500 170 470 0 480Z" fill="var(--sun)"/>
    <path d="M0 480 C170 470 330 500 457 430 L457 520 L0 520Z" fill="var(--leaf)"/>
    <path d="M150 505 C280 500 380 470 457 430 L457 455 C380 490 280 510 150 505Z" fill="var(--leaf-light)"/>
  </svg>
  <h2 class="motto">MAKING LIFE MORE<br>MEANINGFUL (MOTTO)</h2>
  <div class="bio">
    <p>Elise Marchand is a Registered Clinical Counsellor with over 16 years of experience helping people find meaning and transformation in life’s most difficult circumstances.</p>
    <p>She uses cutting edge psychotherapeutic approaches, along with warmth, compassion and humour. Her specialty training in somatic approaches to healing is particularly useful for people with chronic health problems, recovering from accidents, or seeking better awareness of the connection between their minds and their bodies.</p>
  </div>
</section>
</body>
</html>
```